Wordpress Design

A full creative brief is enclosed as well as examples of websites that we feel appropiate for the client. The logo has been designed now, so its a matter of utilizing that brand, and creating a strong "less is more approach"

Better to have dropdowns and information on secondary pages than everything upfront.
Stylish, made in wordpress for easy updates and changes, architectually easy, HTML5 or later.. video compatable, along with severe database collection points.

Target Market(s)

business owners, sophisticated market, CEO's, corporates.Trendy.

Requirements
Must have
• video on opening page as a feature, login details for clients, take advantage of the full screen functionality of HTML5.
Drop downs on entry level 2 pages.
Space for carefully designed banner advertising.
Nice to have
• Full motion video, if we can. We have used templates with this in the past, it maybe too much at this stage however, but we will be creating a video on explainations, anyway.
Should not have
• constrained, or in frames. Not everything on the front page.

```html
<!DOCTYPE html>
<html lang="en">
<head>
<meta charset="utf-8">
<title>Stakeline — Racehorse Syndication</title>
<link href="https://fonts.googleapis.com/css2?family=PT+Sans:wght@400;700&family=PT+Sans+Narrow:wght@400;700&display=swap" rel="stylesheet">
<style>
:root{
  --sky:#1b8fd7;
  --sky-dark:#0f77bd;
  --navy:#0f3a5f;
  --navy-deep:#0c2c4a;
  --band:#1591d9;
  --text:#3d3d3d;
  --muted:#5a5a5a;
  --page:#eef0f2;
  --white:#ffffff;
  --orange:#f36f12;
  --link-light:#ffffff;
}
*{margin:0;padding:0;box-sizing:border-box}
html,body{width:1182px;height:1200px;overflow:hidden}
body{position:relative;font-family:"PT Sans",sans-serif;color:var(--text);
  background:linear-gradient(#f7f8f9 0,#eceef0 900px,var(--navy) 938px,var(--navy-deep) 1200px);}
.abs{position:absolute}
.topbar{left:0;top:0;width:1182px;height:28px;background:linear-gradient(#2aa0e6,var(--sky-dark))}
.client-login{left:916px;top:6px;color:var(--white);font-size:13px;display:flex;align-items:center;gap:10px}
.header{left:0;top:28px;width:1182px;height:122px;background:linear-gradient(#e9f3fb,#ffffff 50%)}
.brand{left:165px;top:70px;font-size:42px;font-weight:700;color:var(--sky);display:flex;align-items:center;gap:10px;letter-spacing:-.5px}
.brand .mark{width:16px;height:16px;background:var(--sky);border-radius:50%}
.ad-banner{left:403px;top:72px;width:425px;height:53px;border:2px solid #22344a;
  background:linear-gradient(90deg,#42617f,#7f8fa0 30%,#3d5e82 60%,#2d4e76)}
.follow{left:956px;top:44px;font-size:13px;color:var(--sky)}
.socials{left:914px;top:67px;display:flex;gap:7px}
.socials span{width:19px;height:19px;border-radius:3px}
.search{left:848px;top:105px;width:159px;height:26px;border:1px solid #cfd4d9;background:var(--white);font-size:12px;color:#444;padding:5px 8px}
.search svg{position:absolute;right:6px;top:5px}
.nav{left:0;top:150px;width:1182px;height:29px;background:linear-gradient(#1d5384,#0d3258);border-top:2px solid #2c6a9f}
.nav a{position:absolute;top:5px;color:var(--white);font-size:12px;text-decoration:none;white-space:nowrap}
.nav i{position:absolute;top:0;width:1px;height:27px;background:#3a6590}
.slider{left:164px;top:193px;width:854px;height:349px;background:var(--white);box-shadow:0 2px 6px rgba(0,0,0,.25)}
.slide-photo{left:7px;top:9px;width:839px;height:331px;background:linear-gradient(#6f8a6a 0,#c8ccc3 30%,#7a5a3a 50%,#5f8f3a 70%,#4e7d2e)}
.thumbs{left:330px;top:503px;width:532px;height:79px;background:var(--white);box-shadow:0 1px 4px rgba(0,0,0,.2)}
.thumb{top:7px;width:95px;height:63px;border:1px solid #c8c8c8;background:linear-gradient(#7a9a6a,#8a5c38 55%,#5e8b3a)}
.arrow-btn{width:20px;height:20px;border-radius:50%;background:var(--sky);display:flex;align-items:center;justify-content:center}
.welcome-box{left:164px;top:603px;width:851px;height:203px;border:1px dashed #b9bcbf;background:#eceeef}
.welcome-photo{left:178px;top:643px;width:137px;height:140px;border:1px solid #c9c9c9;background:linear-gradient(#7c8f6a,#c6a0a8 40%,#3a3030 65%,#5e8a3a)}
.welcome-title{left:333px;top:636px;font-family:"PT Sans Narrow",sans-serif;font-size:21px;color:var(--sky);display:flex;align-items:baseline;gap:8px}
.welcome-title b{font-family:"PT Sans",sans-serif;font-size:26px;font-weight:700}
.welcome-text{left:335px;top:673px;width:348px;font-size:12px;line-height:19px;color:var(--muted);text-align:justify}
.vdiv{left:699px;top:620px;height:172px;border-left:1px dotted #9a9a9a}
.news-title{left:719px;top:618px;font-family:"PT Sans Narrow",sans-serif;font-size:21px;color:var(--sky)}
.news-rule{left:721px;top:645px;width:275px;border-top:1px dotted #8a8a8a}
.news-item{left:722px;width:272px;display:flex;gap:14px;font-size:12px;line-height:17px;color:var(--muted);text-align:justify}
.news-item p{flex:1}
.news-sep{left:722px;width:272px;border-top:1px solid #d4d6d8}
.band{left:164px;top:817px;width:854px;height:207px;background:var(--band)}
.col-title{font-family:"PT Sans Narrow",sans-serif;font-size:21px;color:var(--white)}
.col-rule{height:1px;background:rgba(255,255,255,.35)}
.col-div{top:822px;height:196px;border-left:1px dotted rgba(255,255,255,.55)}
.video{left:185px;top:868px;width:237px;height:144px;background:linear-gradient(#7b8e5a,#6b3a22 45%,#22324a 85%,#222)}
.video-bar{left:185px;top:1000px;width:237px;height:12px;background:#1b1b1b}
.play{left:282px;top:916px;width:38px;height:38px;border-radius:50%;background:rgba(210,40,40,.8);display:flex;align-items:center;justify-content:center}
.gallery-img{left:467px;top:872px;width:256px;height:136px;border:3px solid var(--white);background:linear-gradient(#5c7c3a,#9bb26a 40%,#a56a3a 60%,#8aa44e)}
.bob-link{left:760px;display:flex;align-items:center;gap:13px;font-size:12px;color:var(--link-light);text-decoration:underline}
.foot-links{left:163px;top:1046px;width:450px;font-size:12px;color:#e6eef5;line-height:23px}
.foot-links span{margin:0 6px;color:#9fb4c8}
.foot-rule{left:163px;top:1102px;width:439px;height:1px;background:#2c5579}
.copyright{left:161px;top:1124px;font-size:12px;color:#e6eef5}
.nl-title{left:735px;top:1043px;font-family:"PT Sans Narrow",sans-serif;font-size:21px;color:var(--white)}
.nl-rule{left:735px;top:1074px;width:283px;height:1px;background:#2c5579}
.nl-input{left:736px;top:1091px;width:281px;height:29px;border-radius:4px;background:var(--white);font-size:11px;color:#444;padding:7px 10px}
.nl-submit{left:958px;top:1135px;width:61px;height:26px;border-radius:4px;background:linear-gradient(#ff8a2a,var(--orange));color:var(--white);font-size:13px;display:flex;align-items:center;justify-content:center}
</style>
</head>
<body>
<div class="abs topbar"></div>
<div class="abs client-login">
  <svg width="15" height="15" viewBox="0 0 15 15"><circle cx="7.5" cy="4.5" r="3.2" fill="#fff"/><path d="M1 15c0-4 3-6 6.5-6s6.5 2 6.5 6z" fill="#fff"/></svg>
  CLIENT LOGIN
</div>
<div class="abs header"></div>
<div class="abs brand"><span class="mark"></span>Stakeline</div>
<div class="abs ad-banner" role="img" aria-label="Advertising banner: sponsor artwork"></div>
<div class="abs follow">Follow Us</div>
<div class="abs socials">
  <span style="background:#3b5b9a"></span><span style="background:#33b8e8"></span><span style="background:#f18b21"></span><span style="background:#1a7fbf"></span>
</div>
<div class="abs search">Search
  <svg width="16" height="16" viewBox="0 0 16 16"><circle cx="6.5" cy="6.5" r="4.5" fill="none" stroke="#888" stroke-width="1.6"/><path d="M10 10l5 5" stroke="#888" stroke-width="2"/></svg>
</div>

<nav class="abs nav">
  <a style="left:178px">Home</a><i style="left:230px"></i>
  <a style="left:249px">About Us</a><i style="left:319px"></i>
  <a style="left:335px">Community News</a><i style="left:441px"></i>
  <a style="left:462px">Best of Breed</a><i style="left:555px"></i>
  <a style="left:574px">Buying Syndication Shares</a><i style="left:730px"></i>
  <a style="left:758px">Racing Information</a><i style="left:883px"></i>
  <a style="left:910px">Joining Stakeline</a>
</nav>

<div class="abs slider">
  <div class="abs slide-photo" role="img" aria-label="Racehorses with jockeys galloping on a grass track"></div>
</div>
<div class="abs thumbs">
  <div class="abs thumb" style="left:13px" role="img" aria-label="Race thumbnail"></div>
  <div class="abs thumb" style="left:118px" role="img" aria-label="Horse standing thumbnail"></div>
  <div class="abs thumb" style="left:220px" role="img" aria-label="Horse parade thumbnail"></div>
  <div class="abs thumb" style="left:322px" role="img" aria-label="Race finish thumbnail"></div>
  <div class="abs thumb" style="left:425px" role="img" aria-label="Horse training thumbnail"></div>
</div>
<div class="abs arrow-btn" style="left:319px;top:532px"><svg width="8" height="10"><path d="M6 1L2 5l4 4" fill="none" stroke="#fff" stroke-width="2"/></svg></div>
<div class="abs arrow-btn" style="left:853px;top:532px"><svg width="8" height="10"><path d="M2 1l4 4-4 4" fill="none" stroke="#fff" stroke-width="2"/></svg></div>

<section class="abs welcome-box"></section>
<div class="abs welcome-photo" role="img" aria-label="Jockey on a racehorse in the mounting yard"></div>
<h2 class="abs welcome-title">Welcome to <b>Stakeline</b></h2>
<p class="abs welcome-text">When considering becoming a thoroughbred horse owner, there are many detailed processes to take into consideration when entering the racing industry. Racehorse ownership is an exciting experience that can build friendships, business networks; create wealth, knowledge of the industry and of course an incredible social connection with fashion at the racetrack.&nbsp; So, how do you buy a racehorse?</p>
<div class="abs vdiv"></div>
<h3 class="abs news-title">News And Events</h3>
<div class="abs news-rule"></div>
<div class="abs news-item" style="top:661px"><svg width="18" height="18" viewBox="0 0 18 18"><rect x="1" y="3" width="13" height="14" fill="#fff" stroke="#999"/><path d="M7 12l9-9" stroke="#d9a520" stroke-width="2"/></svg><p>Lorem Ipsum is simply dummy text of the printing and typesetting industry.</p></div>
<div class="abs news-sep" style="top:700px"></div>
<div class="abs news-item" style="top:711px"><svg width="18" height="18" viewBox="0 0 18 18"><rect x="1" y="3" width="13" height="14" fill="#fff" stroke="#999"/><path d="M7 12l9-9" stroke="#d9a520" stroke-width="2"/></svg><p>Lorem Ipsum is simply dummy text of the printing and typesetting industry.</p></div>
<div class="abs news-sep" style="top:752px"></div>
<div class="abs news-item" style="top:763px"><svg width="18" height="18" viewBox="0 0 18 18"><rect x="1" y="3" width="13" height="14" fill="#fff" stroke="#999"/><path d="M7 12l9-9" stroke="#d9a520" stroke-width="2"/></svg><p>Lorem Ipsum is simply dummy text of the printing and typesetting industry.</p></div>

<section class="abs band"></section>
<h3 class="abs col-title" style="left:178px;top:828px">Video</h3>
<div class="abs col-rule" style="left:178px;top:856px;width:251px"></div>
<div class="abs video" role="img" aria-label="Video still of a horse race"></div>
<div class="abs play"><svg width="14" height="16"><path d="M2 1l11 7-11 7z" fill="#fff"/></svg></div>
<div class="abs video-bar"><div style="position:absolute;left:0;top:0;width:118px;height:3px;background:#d01c1c"></div></div>
<div class="abs col-div" style="left:452px"></div>

<h3 class="abs col-title" style="left:469px;top:828px">Gallery</h3>
<svg class="abs" style="left:698px;top:836px" width="26" height="12"><path d="M6 1L2 6l4 5M20 1l4 5-4 5" fill="none" stroke="#fff" stroke-width="2"/></svg>
<div class="abs col-rule" style="left:469px;top:856px;width:254px"></div>
<div class="abs gallery-img" role="img" aria-label="Rider on a chestnut horse in a field"></div>
<div class="abs col-div" style="left:736px"></div>

<h3 class="abs col-title" style="left:751px;top:828px">Best of Bread</h3>
<div class="abs col-rule" style="left:751px;top:856px;width:252px"></div>
<a class="abs bob-link" style="top:873px"><svg width="8" height="8"><path d="M1 0l6 4-6 4z" fill="#fff"/></svg>Approved Syndicators in Australia</a>
<a class="abs bob-link" style="top:900px"><svg width="8" height="8"><path d="M1 0l6 4-6 4z" fill="#fff"/></svg>Approved Syndicators in NZ</a>
<a class="abs bob-link" style="top:927px"><svg width="8" height="8"><path d="M1 0l6 4-6 4z" fill="#fff"/></svg>Approved Syndicators in UK</a>
<a class="abs bob-link" style="top:955px"><svg width="8" height="8"><path d="M1 0l6 4-6 4z" fill="#fff"/></svg>Approved Syndicators in Asia / Pacific</a>
<a class="abs bob-link" style="top:982px"><svg width="8" height="8"><path d="M1 0l6 4-6 4z" fill="#fff"/></svg>Approved Syndicators in South Africa</a>

<footer>
  <div class="abs foot-links">Home<span>|</span>About Us<span>|</span>Community News<span>|</span>Best of Breed<span>|</span>Buying Syndication Shares<span>|</span><br>Racing Information<span>|</span>Joining Stakeline</div>
  <div class="abs foot-rule"></div>
  <div class="abs copyright">Copyrights @ 2012 All Rights Reserved</div>
  <h3 class="abs nl-title">Newsletter</h3>
  <div class="abs nl-rule"></div>
  <div class="abs nl-input">Enter your Email id</div>
  <div class="abs nl-submit">Submit</div>
</footer>
</body>
</html>
```